New Business Card Design Project

We require a business card design for Zelvaquin, a newly established Indian company.
Our focus is on the development, manufacturing, and export of a diverse array of pharmaceutical products on a global scale. The card should convey a professional appearance, as our primary markets are in Africa, China, and Southeast Asian nations.
We envision a two-sided business card, with the reverse side dedicated to a logo set against a solid color or an elegantly designed pattern. The corners should be rounded. We would appreciate seeing both horizontal and vertical design options. We trust the designer to utilize their expertise in creating this design.

The content for the business card is included in the attached Word file.

Target Market(s)

Our primary markets are in Africa, China, and Southeast Asian, Latin America, Maldives, Sri Lanka

Industry/Entity Type

Pharmaceutical Manufacturing and Export

Contact Information for Business Card

Colors

Designer to choose colors to be used in the design.

Requirements
Must have
• The reverse side of the business card features solely the logo along with the tagline, "Remedies of Life."
Should not have
• The logo should not exceed two instances, encompassing both the front and back sides of the card.

```html
<!DOCTYPE html>
<html lang="en">
<head>
<meta charset="utf-8">
<title>Zelvaquin Business Card</title>
<link rel="stylesheet" href="https://fonts.googleapis.com/css2?family=Arimo:wght@400;700&display=swap">
<style>
  :root {
    --stage: #2b2b2d;
    --card-dark: #25252a;
    --card-light: #ffffff;
    --brand-blue: #2aa7df;
    --brand-red: #ef5d4a;
    --ink-light: #ffffff;
  }
  * { margin: 0; padding: 0; box-sizing: border-box; }
  html, body {
    width: 1200px; height: 900px; overflow: hidden;
    background: var(--stage);
    font-family: "Arimo", Arial, sans-serif;
  }
  .canvas { position: relative; width: 1200px; height: 900px; }
  .card {
    position: absolute; left: 250px;
    width: 700px; height: 400px;
    border-radius: 22px; overflow: hidden;
    box-shadow: 0 14px 30px rgba(0,0,0,.45);
  }
  .card-back { top: 35px; background: var(--card-dark); }
  .card-front { top: 465px; background: var(--card-light); }

  .brand-name {
    position: absolute;
    font-weight: 700; color: var(--brand-blue);
    letter-spacing: 1px; line-height: 1;
  }
  .card-back .brand-name { right: 50px; bottom: 70px; font-size: 66px; }

  .wave { position: absolute; inset: 0; width: 700px; height: 400px; }

  .brand-block { position: absolute; right: 55px; top: 45px; text-align: center; width: 330px; }
  .brand-dot {
    width: 30px; height: 30px; border-radius: 50%;
    background: var(--brand-red); margin: 0 auto 20px;
  }
  .card-front .brand-name { position: static; font-size: 62px; }

  .person { position: absolute; left: 48px; top: 188px; color: var(--ink-light); }
  .person-name { font-size: 28px; font-weight: 700; }
  .person-role { font-size: 20px; margin-top: 2px; }
  .person-rule { width: 22px; height: 2px; background: var(--ink-light); margin: 12px 0 12px; }
  .contact-list { list-style: none; font-size: 20px; }
  .contact-list li { display: flex; align-items: center; gap: 10px; margin-bottom: 6px; }
  .contact-list svg { width: 18px; height: 18px; flex: none; }

  .address {
    position: absolute; right: 55px; bottom: 14px;
    color: var(--ink-light); font-size: 20px; font-style: normal;
    text-align: right; line-height: 1.25;
  }
</style>
</head>
<body>
<main class="canvas">
  <section class="card card-back" aria-label="Card back">
    <div class="brand-name">Zelvaquin</div>
  </section>

  <section class="card card-front" aria-label="Card front">
    <svg class="wave" viewBox="0 0 700 400" aria-hidden="true">
      <path d="M0,150 C110,100 220,110 330,200 C420,275 510,310 590,312 C640,312 675,302 700,292 L700,400 L0,400 Z" fill="var(--brand-blue)"/>
      <path d="M0,130 C100,85 210,90 300,140" fill="none" stroke="var(--brand-red)" stroke-width="7"/>
      <path d="M40,140 C130,102 230,115 330,190 C410,250 470,280 520,292" fill="none" stroke="var(--card-light)" stroke-width="3"/>
      <path d="M480,290 C545,306 630,305 700,268" fill="none" stroke="var(--brand-red)" stroke-width="8"/>
    </svg>

    <div class="brand-block">
      <div class="brand-dot"></div>
      <div class="brand-name">Zelvaquin</div>
    </div>

    <div class="person">
      <div class="person-name">Ravin K. Solanke</div>
      <div class="person-role">CEO</div>
      <div class="person-rule"></div>
      <ul class="contact-list">
        <li>
          <svg viewBox="0 0 24 24" fill="none" stroke="#fff" stroke-width="2"><path d="M5 3h4l2 5-3 2a12 12 0 0 0 6 6l2-3 5 2v4a2 2 0 0 1-2 2A17 17 0 0 1 3 5a2 2 0 0 1 2-2z"/></svg>
          +919876501234
        </li>
        <li>
          <svg viewBox="0 0 24 24" fill="none" stroke="#fff" stroke-width="2"><rect x="3" y="5" width="18" height="14" rx="1"/><path d="M3 6l9 7 9-7"/></svg>
          rsolanke@zelvaquin.com
        </li>
        <li>
          <svg viewBox="0 0 24 24" fill="none" stroke="#fff" stroke-width="2"><circle cx="12" cy="12" r="9"/><path d="M3 12h18M12 3c3 3 3 15 0 18M12 3c-3 3-3 15 0 18"/></svg>
          www.zelvaquin.com
        </li>
      </ul>
    </div>

    <address class="address">
      12, Sarovar Nagar<br>Nandpur, 441208, India
    </address>
  </section>
</main>
</body>
</html>
```